Business card design for engineering firm specializing in defense industry.

We need a professional business card design. Something simple but stands out. We are an engineering company specializing in composites in the defense industry.
Industry/Entity Type
Defense
Contact Information for Business Card
A simple black business card with the Varlonix yellow color is what we had in mind but open for other designs.
Colors
ffc214

```html
<!DOCTYPE html>
<html lang="en">
<head>
<meta charset="UTF-8">
<title>Varlonix Business Card</title>
<link href="https://fonts.googleapis.com/css2?family=Exo+2:wght@700&family=Open+Sans:wght@400;600&display=swap" rel="stylesheet">
<style>
  :root {
    --brand-yellow: #ffc214;
    --card-black: #0b0b0b;
    --ink-white: #ffffff;
    --ink-soft: #d9d9d9;
    --page-bg: #eef1f2;
  }
  * { box-sizing: border-box; margin: 0; padding: 0; }
  html, body { width: 800px; height: 1200px; overflow: hidden; }
  body {
    background: var(--page-bg);
    font-family: "Open Sans", Arial, sans-serif;
    position: relative;
  }
  .card {
    position: absolute;
    left: 90px;
    width: 620px;
    height: 354px;
    background: var(--card-black);
    overflow: hidden;
    box-shadow: 0 6px 18px rgba(0,0,0,0.18);
  }
  .card--front { top: 190px; }
  .card--back { top: 620px; }

  /* Front */
  .front-brand {
    position: absolute;
    top: 118px;
    left: 0; right: 0;
    display: flex;
    justify-content: center;
    align-items: center;
    gap: 16px;
  }
  .brand-square {
    width: 26px; height: 26px;
    background: var(--brand-yellow);
  }
  .brand-name {
    font-family: "Exo 2", Arial, sans-serif;
    font-weight: 700;
    color: var(--ink-white);
    font-size: 64px;
    letter-spacing: 0.5px;
    line-height: 1;
  }
  .front-strip {
    position: absolute;
    left: 0; bottom: 0;
    width: 100%; height: 46px;
  }
  .front-url {
    position: absolute;
    bottom: 10px; left: 0; right: 0;
    text-align: center;
    font-size: 13px;
    font-weight: 600;
    color: var(--card-black);
  }

  /* Back */
  .back-trim {
    position: absolute;
    top: 0; left: 0;
    width: 100%; height: 22px;
  }
  .back-name {
    position: absolute;
    top: 40px; left: 34px;
    font-family: "Exo 2", Arial, sans-serif;
    font-weight: 700;
    color: var(--ink-white);
    font-size: 28px;
  }
  .contact-list {
    position: absolute;
    left: 34px; top: 196px;
    list-style: none;
    color: var(--ink-soft);
    font-size: 13px;
  }
  .contact-item {
    display: flex;
    align-items: flex-start;
    gap: 12px;
    margin-bottom: 18px;
    line-height: 1.45;
  }
  .contact-icon { width: 16px; height: 16px; flex: none; margin-top: 2px; }
</style>
</head>
<body>

<section class="card card--front" aria-label="Business card front">
  <div class="front-brand">
    <span class="brand-square"></span>
    <span class="brand-name">Varlonix</span>
  </div>
  <svg class="front-strip" viewBox="0 0 620 46" preserveAspectRatio="none" aria-hidden="true">
    <polygon points="0,20 150,20 172,6 448,6 470,20 620,20 620,46 0,46" fill="#ffc214"/>
  </svg>
  <p class="front-url">www.varlonixinc.com</p>
</section>

<section class="card card--back" aria-label="Business card back">
  <svg class="back-trim" viewBox="0 0 620 22" preserveAspectRatio="none" aria-hidden="true">
    <polygon points="0,0 620,0 620,6 300,6 286,0" fill="#ffc214"/>
    <rect x="0" y="0" width="620" height="4" fill="#ffc214"/>
  </svg>
  <h1 class="back-name">Varlonix</h1>
  <ul class="contact-list">
    <li class="contact-item">
      <svg class="contact-icon" viewBox="0 0 16 16" aria-hidden="true">
        <rect x="1.5" y="3.5" width="13" height="9" fill="none" stroke="#ffc214" stroke-width="1.4"/>
        <polyline points="1.5,3.5 8,9 14.5,3.5" fill="none" stroke="#ffc214" stroke-width="1.4"/>
      </svg>
      <span>support@varlonixtech.com</span>
    </li>
    <li class="contact-item">
      <svg class="contact-icon" viewBox="0 0 16 16" aria-hidden="true">
        <circle cx="8" cy="8" r="6.3" fill="none" stroke="#ffc214" stroke-width="1.4"/>
        <ellipse cx="8" cy="8" rx="2.8" ry="6.3" fill="none" stroke="#ffc214" stroke-width="1.2"/>
        <line x1="1.7" y1="8" x2="14.3" y2="8" stroke="#ffc214" stroke-width="1.2"/>
      </svg>
      <span>www.varlonixinc.com</span>
    </li>
    <li class="contact-item">
      <svg class="contact-icon" viewBox="0 0 16 16" aria-hidden="true">
        <path d="M8 15 C8 15 3 9.5 3 6.2 A5 5 0 0 1 13 6.2 C13 9.5 8 15 8 15 Z" fill="none" stroke="#ffc214" stroke-width="1.4"/>
        <circle cx="8" cy="6.2" r="1.8" fill="#ffc214"/>
      </svg>
      <span>Varlonix, Inc.<br>82 Harlow Avenue<br>Dunmore, Vermont 05321</span>
    </li>
  </ul>
</section>

</body>
</html>
```